Poster Needed for Church Conference

I need a poster for a weekend conference at my church. Looking to attract as many people as possible. We are a church in the suburbs of Houston. This is mainly for our own church members but we are opening it up to outside church members.

Please see previous design from last conference and all other graphic work that can (doesn't need to be) included.

Target Market(s)

It's targeted for all people. But our main audience is families. around the age of 30 should be main target.

Industry/Entity Type

Non-Profit

Font styles to use
Serif
Sans Serif

Colors

Designer to choose colors to be used in the design.

Requirements
Must have
• 11x17 design with ability to shrink and blow up. but ideally for 11x17
• Content and wording:
• "Rooted Lantern Conference: Bridging the gap between generations and passing on our deepest beliefs and values."
• Featuring Dr. Glen Marlowe. Author of "The Map of Q9"
• Aug 25-26: Friday 8-10 pm, Saturday 4-8 pm
• Cost Adults $15/Children $5: Covers admission to all sessions and workshops, refreshments and Saturday dinner. *kids 5 and under free
• Childcare provided for all sessions. "
• Please use church logo and address on flyer: 4312 Orchard Bend, Missouri City, TX 77512
Nice to have
• Ideally it will be designed so that we can crop a 16:9 pp announcement slide and header for our website.
Should not have
• anything offensive

```html
<!DOCTYPE html>
<html lang="en">
<head>
<meta charset="utf-8">
<title>Rooted Lantern Conference Poster</title>
<link href="https://fonts.googleapis.com/css2?family=Anton&family=Roboto+Condensed:wght@700&family=Handlee&family=Arimo:ital,wght@0,400;0,700;1,400&display=swap" rel="stylesheet">
<style>
  :root {
    --pink: #e6007e;
    --sky: #4fc3ee;
    --green: #62b946;
    --green-deep: #58ad3d;
    --note: #f8f29c;
    --note-shade: #e9e07a;
    --ink: #333333;
    --paper: #ffffff;
    --backdrop: #ececec;
  }
  * { margin: 0; padding: 0; box-sizing: border-box; }
  html, body { width: 1200px; height: 900px; overflow: hidden; background: var(--backdrop); }
  .canvas { position: relative; width: 1200px; height: 900px; }
  .poster {
    position: absolute; left: 329px; top: 29px; width: 541px; height: 837px;
    background: var(--paper); overflow: hidden;
    font-family: "Arimo", Arial, sans-serif; color: var(--ink);
  }
  .poster-art { position: absolute; inset: 0; }
  .title { position: absolute; left: 0; top: 0; width: 541px; height: 200px; }
  .title text { font-family: "Anton", "Impact", sans-serif; }
  .tagline {
    position: absolute; left: 18px; top: 208px; width: 500px; height: 85px;
    display: flex; align-items: center; justify-content: center; text-align: center;
    font-family: "Handlee", cursive; font-style: italic; font-size: 19px; line-height: 1.2; color: var(--ink);
  }
  .details { position: absolute; left: 36px; top: 310px; width: 260px; }
  .label {
    font-family: "Roboto Condensed", "Arial Narrow", sans-serif; font-weight: 700;
    font-size: 26px; line-height: 1;
  }
  .label-featuring { color: var(--pink); }
  .label-date { color: var(--sky); margin-top: 16px; }
  .label-cost { color: var(--green); margin-top: 20px; }
  .speaker-name {
    font-family: "Roboto Condensed", "Arial Narrow", sans-serif; font-weight: 700;
    font-size: 26px; color: var(--ink); margin-top: 12px; line-height: 1;
  }
  .speaker-book { font-style: italic; font-size: 13px; margin-top: 4px; }
  .schedule { font-size: 16px; line-height: 23px; margin-top: 6px; }
  .price { font-size: 15px; margin-top: 8px; }
  .notes { list-style: none; margin-left: -14px; margin-top: 4px; font-style: italic; font-size: 13px; line-height: 16.5px; }
  .notes li { position: relative; padding-left: 14px; }
  .notes li::before { content: "•"; position: absolute; left: 0; font-style: normal; }
  .notes li + li { margin-top: 2px; }
  .notes li:nth-child(2) { margin-top: 6px; }
  .venue { position: absolute; left: 36px; top: 670px; }
  .venue-name { color: var(--green); font-size: 16px; line-height: 18px; }
  .venue-address { font-size: 12px; font-weight: 700; line-height: 16px; margin-top: 8px; }
  .church-name {
    position: absolute; left: 272px; top: 744px; display: flex; align-items: center; gap: 10px;
    color: var(--paper); font-size: 19px; line-height: 21px; font-weight: 400; letter-spacing: 1px;
  }
  .church-mark { width: 22px; height: 22px; background: var(--paper); flex: none; }
</style>
</head>
<body>
<div class="canvas">
  <div class="poster">
    <svg class="poster-art" width="541" height="837" viewBox="0 0 541 837">
      <defs>
        <radialGradient id="portraitTone" cx="50%" cy="40%" r="60%">
          <stop offset="0" stop-color="#e7c2ac"/>
          <stop offset="0.6" stop-color="#c99d86"/>
          <stop offset="1" stop-color="#8d8d8d"/>
        </radialGradient>
        <linearGradient id="bookTone" x1="0" y1="0" x2="0" y2="1">
          <stop offset="0" stop-color="#f1f1f1"/>
          <stop offset="1" stop-color="#cfd8cc"/>
        </linearGradient>
      </defs>
      <!-- sticky note -->
      <rect x="20" y="211" width="500" height="85" fill="var(--note-shade)" opacity="0.5"/>
      <rect x="18" y="208" width="500" height="85" fill="var(--note)"/>
      <path d="M18 208 L48 208 L18 238 Z" fill="var(--paper)"/>
      <path d="M48 208 L18 238 L44 234 Z" fill="var(--note-shade)"/>
      <!-- bottom swoosh -->
      <path d="M0 837 L0 784 C230 765 470 680 541 480 L541 837 Z" fill="var(--green)"/>
      <!-- ring -->
      <circle cx="410" cy="500" r="96" fill="none" stroke="var(--green)" stroke-width="20"/>
      <!-- portrait -->
      <path d="M308 390 C300 330 340 305 400 305 C460 305 488 345 478 410 C470 470 470 535 455 560 L330 560 C320 520 315 450 308 390 Z"
            fill="url(#portraitTone)" role="img" aria-label="Portrait photo of the featured speaker"/>
      <!-- book -->
      <g transform="rotate(-6 260 490)">
        <rect x="208" y="418" width="108" height="150" fill="url(#bookTone)" stroke="#bdbdbd" stroke-width="1"
              role="img" aria-label="Cover of the speaker's book"/>
        <rect x="208" y="520" width="108" height="16" fill="var(--green)" opacity="0.8"/>
      </g>
    </svg>

    <svg class="title" viewBox="0 0 541 200" role="heading" aria-level="1">
      <text x="18" y="112" font-size="76" textLength="505" lengthAdjust="spacingAndGlyphs">
        <tspan fill="var(--pink)">ROOTED</tspan> <tspan fill="var(--sky)">LANTERN</tspan>
      </text>
      <text x="32" y="194" font-size="92" fill="var(--green)" textLength="488" lengthAdjust="spacingAndGlyphs">CONFERENCE</text>
    </svg>

    <p class="tagline">Bridging the gap between generations<br>and passing on our deepest beliefs and values.</p>

    <section class="details">
      <h2 class="label label-featuring">Featuring</h2>
      <p class="speaker-name">Dr. Glen Marlowe</p>
      <p class="speaker-book">Author of "The Map of Q9"</p>
      <h2 class="label label-date">Aug 25-26</h2>
      <p class="schedule">Friday 8-10 pm<br>Saturday 4-8 pm</p>
      <h2 class="label label-cost">Cost</h2>
      <p class="price">Adults $15/ Children $5</p>
      <ul class="notes">
        <li>Covers admission to all sessions<br>and workshops, refreshments<br>and Saturday dinner.</li>
        <li>kids 5 and under free</li>
        <li>Childcare provided for all sessions.</li>
      </ul>
    </section>

    <address class="venue" style="font-style: normal;">
      <p class="venue-name">Cedar Hollow<br>Community Church</p>
      <p class="venue-address">4312 Orchard Bend,<br>Missouri City,<br>TX 77512</p>
    </address>

    <div class="church-name">
      <span class="church-mark"></span>
      <span>cedar hollow<br>community church</span>
    </div>
  </div>
</div>
</body>
</html>
```